Brochure Design Project for Whole Body Cryotherapy

We need a dynamic and call to action brochure of our new whole body cryotherapy. Focusing on Weight loss, sports performance, health and pain relief management. Complete with testimonials, media, users, and complete design and branding using our brand guidelines.

Target Market(s)

people who are aesthetics and health conscious. Plus people who are in for the latest and most hyped technology available

Industry/Entity Type

Health

Requirements
Must have
• important media and users . researching is important. we are in asia and singapore. its the first ever whole body cryotherapy. therefore is a big launch and totally brand new device. We need to creat a very very big hype.

```html
<!DOCTYPE html>
<html lang="en">
<head>
<meta charset="utf-8">
<title>KRYA Whole Body Cryotherapy — Brochure Cover</title>
<link rel="stylesheet" href="https://fonts.googleapis.com/css2?family=Montserrat:wght@200;700;800&family=Oswald:wght@500&family=Tinos:ital,wght@0,400;1,700&display=swap">
<style>
  :root {
    --panel-deep: #2fa5de;
    --panel-light: #5cc8f8;
    --edge-white: #ffffff;
    --edge-shade: #1b78aa;
    --ink-navy: #17344b;
    --ink-dark: #2f3a44;
    --silver-hi: #f2f4f4;
    --silver-lo: #9aa3a6;
  }
  html, body {
    margin: 0;
    padding: 0;
    width: 1200px;
    height: 2558px;
    overflow: hidden;
    background: var(--panel-light);
  }
  .cover {
    position: relative;
    width: 1200px;
    height: 2558px;
    overflow: hidden;
    background: var(--panel-light);
  }
  .cover__wave {
    position: absolute;
    inset: 0;
    width: 1200px;
    height: 2558px;
  }
  .wave-deep { fill: var(--panel-deep); }
  .wave-edge { fill: var(--edge-white); }
  .wave-line { fill: none; stroke: var(--edge-shade); stroke-width: 5; }
  .benefits-line {
    font-family: "Oswald", sans-serif;
    font-weight: 500;
    font-size: 27px;
    fill: var(--ink-navy);
  }
  .brand-name {
    position: absolute;
    left: 82px;
    top: 1195px;
    margin: 0;
    font-family: "Montserrat", sans-serif;
    font-weight: 800;
    font-size: 116px;
    line-height: 1;
    color: var(--edge-white);
    letter-spacing: -3px;
  }
  .product-name {
    position: absolute;
    left: 532px;
    top: 1248px;
    margin: 0;
    font-family: "Montserrat", sans-serif;
    font-size: 52px;
    line-height: 1;
    color: var(--ink-navy);
    letter-spacing: 1px;
  }
  .product-name__light { font-weight: 200; }
  .product-name__bold { font-weight: 700; }
  .burn-claim {
    position: absolute;
    left: 628px;
    top: 1370px;
    width: 540px;
    height: 140px;
  }
  .burn-claim__lead {
    position: absolute;
    left: 0;
    top: 45px;
    font-family: "Tinos", serif;
    font-size: 27px;
    color: var(--edge-white);
    white-space: nowrap;
  }
  .burn-claim__badge {
    position: absolute;
    left: 172px;
    top: 4px;
    width: 240px;
    height: 104px;
    border-radius: 30px;
    background: linear-gradient(180deg, var(--silver-hi) 0%, #c9cfd1 55%, var(--silver-lo) 100%);
    box-shadow: 0 4px 10px rgba(0, 0, 0, 0.25);
  }
  .burn-claim__amount {
    position: absolute;
    left: 20px;
    top: 13px;
    width: 130px;
    margin: 0;
    font-family: "Tinos", serif;
    font-style: italic;
    font-weight: 700;
    font-size: 33px;
    line-height: 38px;
    text-align: center;
    color: var(--ink-dark);
  }
  .burn-claim__time {
    position: absolute;
    left: 352px;
    top: -36px;
    font-family: "Montserrat", sans-serif;
    font-weight: 800;
    font-size: 165px;
    line-height: 1;
    color: var(--ink-dark);
  }
  .burn-claim__unit {
    position: absolute;
    left: 442px;
    top: 74px;
    font-family: "Tinos", serif;
    font-size: 28px;
    color: var(--ink-dark);
  }
</style>
</head>
<body>
<main class="cover">
  <svg class="cover__wave" viewBox="0 0 1200 2558" aria-label="Wave divider with benefit line">
    <defs>
      <path id="wave-boundary" d="M742,0 C800,90 825,200 812,330 C795,520 700,800 600,1020 C540,1160 495,1320 498,1500 C502,1720 580,1980 680,2200 C740,2340 790,2460 805,2558"/>
      <path id="benefits-path" d="M636,2236 C536,2000 452,1720 448,1500 C445,1320 490,1160 552,1020 C652,800 746,520 762,330"/>
    </defs>
    <path class="wave-edge" d="M760,0 C818,90 845,200 832,330 C815,520 720,800 620,1020 C560,1160 515,1320 518,1500 C522,1720 600,1980 702,2200 C764,2340 814,2460 830,2558 L0,2558 L0,0 Z"/>
    <path class="wave-deep" d="M742,0 C800,90 825,200 812,330 C795,520 700,800 600,1020 C540,1160 495,1320 498,1500 C502,1720 580,1980 680,2200 C740,2340 790,2460 805,2558 L0,2558 L0,0 Z"/>
    <use href="#wave-boundary" class="wave-line"/>
    <text class="benefits-line">
      <textPath href="#benefits-path" textLength="1960" lengthAdjust="spacing">WEIGHT LOSS - SPORTS PERFORMANCE - HEALTH AND PAIN RELIEF MANAGEMENT</textPath>
    </text>
  </svg>

  <h1 class="brand-name">KRYA</h1>

  <p class="product-name"><span class="product-name__light">COLD</span><span class="product-name__bold">CORE</span></p>

  <div class="burn-claim">
    <span class="burn-claim__lead">BURNS UPTO</span>
    <div class="burn-claim__badge">
      <p class="burn-claim__amount">1000 K<br>CALS</p>
    </div>
    <span class="burn-claim__time">2</span>
    <span class="burn-claim__unit">min</span>
  </div>
</main>
</body>
</html>
```